Tax Preparation flyer for LedgerMint Corp.

My Client would like a one page PDF flyer to promote upcoming tax season in Canada. This firm is affordable and all virtual. I have attached a copy of their logo and a word document with the proposed wording for the flyer. Please feel free to change if you have better suggestions.

Target Market(s)

individuals in canada

Colors
0054AA
0677BA
7BADD7
CADEEF
E8F1F8

```html
<!DOCTYPE html>
<html lang="en">
<head>
<meta charset="UTF-8">
<title>LedgerMint Corp. – Tax Season Flyer</title>
<link rel="stylesheet" href="https://fonts.googleapis.com/css2?family=Bebas+Neue&family=Lexend:wght@400;600&family=Montserrat:wght@800;900&family=Poppins:wght@700&family=Kalam:wght@700&display=swap">
<style>
  :root {
    --paper: #efefef;
    --ink: #263238;
    --ink-soft: #2b2b2b;
    --blue: #3a9fe0;
    --white: #ffffff;
    --icon-grey: #c7cacc;
    --accent-red: #e0322b;
  }
  * { margin: 0; padding: 0; box-sizing: border-box; }
  html, body { width: 1200px; height: 3000px; overflow: hidden; }
  body {
    position: relative;
    background: var(--paper);
    font-family: "Lexend", sans-serif;
    color: var(--ink-soft);
  }
  .brand {
    position: absolute; top: 58px; left: 0; width: 1200px;
    text-align: center;
    font-family: "Poppins", sans-serif; font-weight: 700;
    font-size: 62px; color: var(--ink); letter-spacing: -1px;
  }
  .hero {
    position: absolute; top: 202px; left: 0; width: 1200px; height: 298px;
    background: var(--ink); color: var(--white); text-align: center;
    font-family: "Montserrat", sans-serif;
  }
  .hero__title { position: absolute; top: 14px; width: 100%; font-weight: 900; font-size: 168px; line-height: 1; letter-spacing: -2px; }
  .hero__sub { position: absolute; top: 186px; width: 100%; font-weight: 900; font-size: 84px; line-height: 1; }
  .hero__icon { position: absolute; top: 271px; width: 160px; height: 160px; }
  .hero__icon--left { left: 43px; }
  .hero__icon--right { left: 997px; }

  .panel {
    position: absolute; left: 72px; width: 1056px;
    border: 4px solid var(--ink); border-radius: 36px;
  }
  .panel--about { top: 627px; height: 948px; }
  .panel--pricing { top: 1704px; height: 738px; }
  .tab {
    position: absolute; left: 186px; width: 822px; height: 108px;
    background: var(--blue); border-radius: 26px;
    box-shadow: 9px 9px 0 var(--ink);
    font-family: "Bebas Neue", sans-serif; color: var(--white);
    font-size: 62px; line-height: 108px;
  }
  .tab--about { top: 565px; }
  .tab--pricing { top: 1641px; }
  .tab__icon { position: absolute; left: 26px; top: 32px; width: 46px; height: 46px; }
  .tab__label { position: absolute; left: 110px; right: 40px; }
  .tab--pricing .tab__label { text-align: center; left: 0; right: 0; }

  .about__text { position: absolute; left: 117px; top: 712px; width: 980px; font-size: 33px; line-height: 54px; }
  .about__text p + p { margin-top: 54px; }
  .about__text strong { font-weight: 600; color: #111; }

  .price-row {
    position: absolute; left: 118px; width: 964px;
    display: flex; justify-content: space-between;
    font-weight: 600; font-size: 33px; color: #111;
  }
  .price-row--personal { top: 1793px; }
  .price-row--business { top: 1866px; }
  .underline { position: absolute; left: 118px; width: 210px; height: 16px; }
  .underline--personal { top: 1838px; }
  .underline--business { top: 1911px; }

  .note { position: absolute; left: 118px; top: 1982px; width: 966px; }
  .note__label { font-weight: 600; font-size: 31px; color: #111; margin-bottom: 10px; }
  .note__list { list-style: disc; padding-left: 48px; font-size: 26px; line-height: 45px; }

  .tagline {
    position: absolute; top: 2505px; width: 1200px; text-align: center;
    font-family: "Montserrat", sans-serif; font-weight: 800;
    font-size: 64px; line-height: 84px; color: #333;
  }
  .tagline__script { font-family: "Kalam", cursive; font-weight: 700; font-size: 60px; font-style: italic; }

  .contact {
    position: absolute; top: 2737px; left: 0; width: 1200px; height: 170px;
    background: var(--ink); color: var(--white); font-size: 36px;
  }
  .contact__item { position: absolute; top: 0; height: 170px; display: flex; align-items: center; }
  .contact__item--email { left: 114px; }
  .contact__item--phone { left: 648px; }
  .contact__item svg { margin-right: 26px; }
</style>
</head>
<body>
  <div class="brand">LedgerMint Corp.</div>

  <header class="hero">
    <div class="hero__title">RELAX,</div>
    <div class="hero__sub">WE’VE GOT YOU!</div>
  </header>
  <svg class="hero__icon hero__icon--left" viewBox="0 0 160 160" aria-hidden="true">
    <path d="M28 60 A56 56 0 0 1 128 48" fill="none" stroke="var(--icon-grey)" stroke-width="12"/>
    <polygon points="140,30 140,70 106,60" fill="var(--icon-grey)"/>
    <path d="M132 100 A56 56 0 0 1 32 112" fill="none" stroke="var(--icon-grey)" stroke-width="12"/>
    <polygon points="20,130 20,90 54,100" fill="var(--icon-grey)"/>
    <circle cx="80" cy="80" r="42" fill="var(--icon-grey)"/>
    <text x="80" y="104" text-anchor="middle" font-family="Montserrat, sans-serif" font-weight="900" font-size="66" fill="#263238">$</text>
  </svg>
  <svg class="hero__icon hero__icon--right" viewBox="0 0 160 160" aria-hidden="true">
    <path d="M28 60 A56 56 0 0 1 128 48" fill="none" stroke="var(--icon-grey)" stroke-width="12"/>
    <polygon points="140,30 140,70 106,60" fill="var(--icon-grey)"/>
    <path d="M132 100 A56 56 0 0 1 32 112" fill="none" stroke="var(--icon-grey)" stroke-width="12"/>
    <polygon points="20,130 20,90 54,100" fill="var(--icon-grey)"/>
    <circle cx="80" cy="80" r="42" fill="var(--icon-grey)"/>
    <text x="80" y="104" text-anchor="middle" font-family="Montserrat, sans-serif" font-weight="900" font-size="66" fill="#263238">$</text>
  </svg>

  <section class="panel panel--about"></section>
  <div class="tab tab--about">
    <svg class="tab__icon" viewBox="0 0 46 46" aria-hidden="true"><circle cx="19" cy="19" r="14" fill="none" stroke="#263238" stroke-width="4"/><line x1="29" y1="29" x2="42" y2="42" stroke="#263238" stroke-width="4" stroke-linecap="round"/></svg>
    <span class="tab__label">WE’VE GOT YOUR TAXES COVERED!</span>
  </div>
  <div class="about__text">
    <p><strong>Our tax preparers have over 20 years experience and worked both in public accounting firms as well as specialized tax.</strong> Our tax services are virtual, so you don’t have to take the time for a personal visit. We take care of everything and can access all your tax slips from CRA website directly into our tax software. All signing is done via SignVault.</p>
    <p>You can fill and submit the appropriate forms, along with all your other documents, in our secure client portal. It’s important that we understand your situation and any changes in your situation from the past year.</p>
    <p><strong>If you have a complex tax situation and would like to discuss it, we can meet in virtually over MeetLoop or TalkRoom.</strong></p>
  </div>

  <section class="panel panel--pricing"></section>
  <div class="tab tab--pricing">
    <svg class="tab__icon" viewBox="0 0 46 46" aria-hidden="true"><circle cx="19" cy="19" r="14" fill="none" stroke="#263238" stroke-width="4"/><line x1="29" y1="29" x2="42" y2="42" stroke="#263238" stroke-width="4" stroke-linecap="round"/></svg>
    <span class="tab__label">($) PRICING</span>
  </div>
  <div class="price-row price-row--personal"><span>Personal Tax Return</span><span>$100</span></div>
  <svg class="underline underline--personal" viewBox="0 0 210 16" aria-hidden="true"><path d="M4 6 Q100 2 206 4 M10 13 Q60 6 150 9" fill="none" stroke="var(--accent-red)" stroke-width="3" stroke-linecap="round"/></svg>
  <div class="price-row price-row--business"><span>Add a business or rental schedule</span><span>$125/business</span></div>
  <svg class="underline underline--business" viewBox="0 0 210 16" aria-hidden="true"><path d="M4 6 Q100 2 206 4 M10 13 Q60 6 150 9" fill="none" stroke="var(--accent-red)" stroke-width="3" stroke-linecap="round"/></svg>

  <div class="note">
    <div class="note__label">NOTE :</div>
    <ul class="note__list">
      <li>More complex tax returns will be assessed &nbsp;based on the complexity of the return and you will be advised before we start.</li>
      <li>Did you fall behind in filing your income tax save 20% when you file 3 or more years with us. We can do back to 2012 for filing of tax returns.</li>
      <li>If you expect a refund, the earlier you file the sooner you will receive your refund. Our average turn around time prior to April is a couple of days.</li>
    </ul>
  </div>

  <div class="tagline">TODAY SO YOU CAN START<br>TO <span class="tagline__script">breathe</span> EASY.</div>

  <footer class="contact">
    <div class="contact__item contact__item--email">
      <svg width="90" height="58" viewBox="0 0 90 58" aria-hidden="true"><rect x="2" y="2" width="86" height="54" fill="none" stroke="#fff" stroke-width="4"/><path d="M2 2 L45 36 L88 2 M2 56 L36 28 M88 56 L54 28" fill="none" stroke="#fff" stroke-width="4"/></svg>
      <span>hello@ledgermint.ca</span>
    </div>
    <div class="contact__item contact__item--phone">
      <svg width="76" height="76" viewBox="0 0 76 76" aria-hidden="true"><circle cx="38" cy="38" r="36" fill="#fff"/><path d="M26 18 l8 0 4 12 -6 5 q5 10 13 14 l5 -6 12 4 0 8 q-2 6 -9 6 q-18 -2 -30 -21 q-5 -10 -3 -18 q2 -4 6 -4z" fill="#263238"/></svg>
      <span>0000 - 0000 - 000</span>
    </div>
  </footer>
</body>
</html>
```